Curtain and Blind Manufacturers - Retail Ecommerce All Pages

To Design a high converting website design for and improve on the domain www.keelworth-textiles.co.uk.

Generally it is improvements on what already exists, the core layout is functional and strong. Needs to have the header mobile responsive. Core elements for each page and clear content.

Current header is good just needs modernising and needs to work well on mobile. Need a way of having a mixture of categories and advice where necessary.

Pages and detailing required.
Home - Great Imagery for the sections. Category specific. A good product offering. So Call to product. Potentially straight to our best selling products. Not in a slider but in a straight forward grid. A nice simlar design to competitors in my space. shadesquik, my own website. also i like websites like lumo pillows, harrowdene.co.uk needs to be simple with clear direction for the customer particularly on mobile to get them to what we do quickly. EG curtains, blinds etc

Inner pages

Category Top Filters
https://www.keelworth-textiles.co.uk/flame-retardant/curtains

Category Side bar filters

Category Mobile with Off Canvas Filters

Product - Fabric
https://www.keelworth-textiles.co.uk/torvale-flame-retardant-curtain-fabric.html

Product - Curtains - https://www.keelworth-textiles.co.uk/torvale-fr-curtains.html

Product - Blinds
Cart
Checkout
Slide in Cart
Slide in Filters
General Content Page
About

```html
<!DOCTYPE html>
<html lang="en">
<head>
<meta charset="utf-8">
<title>Category Product Page – Keelworth Textiles</title>
<link rel="stylesheet" href="https://fonts.googleapis.com/css2?family=Barlow+Semi+Condensed:wght@600;700&family=Rubik:wght@400;500;600&display=swap">
<style>
:root{
  --page:#efeaeb;
  --ink:#1e1e1e;
  --muted:#6f6f6f;
  --red:#c8202f;
  --blue:#2c4f9a;
  --sort:#707070;
  --panel:#f3f3f3;
  --line:#e2e2e2;
  --white:#ffffff;
  --star:#f2b01e;
  --dark:#2b2b2b;
}
*{box-sizing:border-box;margin:0;padding:0}
html,body{width:1200px;height:747px;overflow:hidden}
body{background:var(--page);font-family:"Rubik",sans-serif;color:var(--ink);position:relative}
.page-title{position:absolute;top:78px;left:0;width:1200px;text-align:center;font-family:"Barlow Semi Condensed",sans-serif;font-weight:700;font-size:29px;letter-spacing:.5px}
.caption{position:absolute;top:650px;width:260px;text-align:center;font-family:"Barlow Semi Condensed",sans-serif;font-weight:700;font-size:12.5px;letter-spacing:.3px}
.screen{position:absolute;width:222px;height:444px;background:var(--white);border-radius:16px;overflow:hidden;box-shadow:0 4px 14px rgba(0,0,0,.08)}
.s1{left:91px;top:175px}.s2{left:352px;top:174px}.s3{left:610px;top:176px}.s4{left:875px;top:178px}

/* header */
.promo{height:21px;background:var(--blue);color:var(--white);font-size:6.6px;font-weight:500;display:flex;align-items:center;justify-content:center;gap:3px}
.masthead{height:41px;display:flex;align-items:center;padding:0 9px;justify-content:space-between}
.brand{display:flex;align-items:center;gap:4px;color:var(--red);font-weight:600;font-size:8.5px;letter-spacing:.2px}
.brand-mark{width:13px;height:13px;background:var(--red)}
.call{display:flex;align-items:center;gap:3px;font-size:6.5px;line-height:1.15}
.call b{display:block;color:var(--red);font-weight:500;font-size:8px}
.cart{width:22px;height:22px;border-radius:50%;background:#f1f1f1;position:relative;display:flex;align-items:center;justify-content:center}
.cart i{position:absolute;top:1px;right:0;width:7px;height:7px;border-radius:50%;background:var(--red);color:#fff;font-size:5px;font-style:normal;display:flex;align-items:center;justify-content:center}
.search-row{height:32px;display:flex;align-items:center;padding:0 9px;gap:10px;border-bottom:1px solid var(--line)}
.burger{width:16px;display:flex;flex-direction:column;gap:3px}
.burger span{height:1.5px;background:var(--red)}
.search{flex:1;height:21px;border:1px solid #d8d8d8;border-radius:3px;font-size:6.5px;color:#9a9a9a;display:flex;align-items:center;justify-content:space-between;padding:0 5px}
.usps{height:37px;display:flex;align-items:center;justify-content:space-between;padding:0 8px;font-size:5.5px;font-weight:500;line-height:1.15;box-shadow:0 2px 3px rgba(0,0,0,.05)}
.usp{display:flex;align-items:center;gap:3px}
.rating{display:flex;align-items:center;gap:3px;font-size:8px;font-weight:500}
.rating em{font-style:normal;background:var(--red);color:#fff;font-size:6.5px;padding:1px 2px;border-radius:2px}
.rating .sq{width:7px;height:7px;background:#00b67a}

/* toolbar */
.toolbar{display:flex;height:34px;font-size:6.2px;color:#fff;font-weight:500}
.filters-btn{width:53%;background:var(--red);display:flex;align-items:center;gap:5px;padding-left:12px}
.sort-btn{flex:1;background:var(--sort);display:flex;align-items:center;justify-content:center;gap:6px;font-weight:400;font-size:6.8px}

/* nav */
.tabbar{position:absolute;bottom:0;left:0;right:0;height:42px;background:#fff;display:flex;justify-content:space-around;align-items:center;border-top:1px solid var(--line)}
.tab{display:flex;flex-direction:column;align-items:center;gap:3px;font-size:6.8px;color:#555}
.tab.active{color:var(--red)}

/* hero */
.hero{position:relative;height:180px}
.hero-photo{position:absolute;inset:0;background:linear-gradient(180deg,#3d3431 0%,#5b463a 45%,#35302e 100%)}
.hero-copy{position:absolute;inset:0;display:flex;flex-direction:column;align-items:center;padding-top:26px;color:#fff;text-align:center}
.hero-rev{font-size:9px;font-weight:500;line-height:1.4}
.hero-rev small{display:block;font-size:8px}
.hero h1{font-size:13px;font-weight:500;line-height:1.15;margin-top:10px}
.hero p{font-size:8px;font-weight:500;margin-top:6px;line-height:1.25}
.quote-btn{margin-top:9px;background:var(--red);font-size:7px;font-weight:500;padding:5px 8px;border-radius:2px}
.trusted{height:52px;background:var(--dark);color:#fff;text-align:center;padding-top:9px;font-size:6.5px;font-weight:500}
.trusted-row{display:flex;align-items:center;justify-content:space-between;padding:0 12px;margin-top:10px}
.partner{font-size:7px;color:#c9c9c9;font-weight:500}
.partner.box{background:#8a8a8a;width:34px;height:11px}

/* listing */
.listing{background:var(--panel);height:237px;padding:0 11px;position:relative}
.crumb{font-size:5.6px;color:#777;padding-top:10px}
.crumb b{font-weight:600;color:#444}
.intro{background:#fff;margin-top:9px;border-radius:3px;padding:8px 10px;font-size:6.6px;color:#555;line-height:1.25;display:flex;justify-content:space-between;align-items:center;box-shadow:0 1px 3px rgba(0,0,0,.06)}
.count{font-size:6.6px;color:#777;margin-top:9px}
.cards{display:flex;gap:10px;margin-top:13px}
.card{flex:1;background:#fff;height:150px;position:relative;text-align:center;padding:7px 6px 0}
.badge{position:absolute;top:-8px;left:50%;transform:translateX(-50%);font-size:6.2px;font-weight:600;padding:2px 9px;border-radius:8px;white-space:nowrap}
.badge.new{background:#e0e0e0;color:var(--red)}
.badge.best{background:var(--red);color:#fff}
.card-photo{height:72px}
.card h3{font-size:6.8px;font-weight:600;line-height:1.2;margin-top:5px}
.stars{color:var(--star);font-size:6.5px;margin-top:1px}
.stars span{color:#777;font-size:5.5px}
.price{font-size:5.5px;color:#666;margin-top:2px;line-height:1.35}
.price b{color:var(--red);font-size:7px;font-weight:500}

/* features */
.features{display:grid;grid-template-columns:1fr 1fr;gap:6px;margin-top:6px}
.feature{background:#fff;border:1px solid #e8e8e8;border-radius:4px;height:96px;display:flex;flex-direction:column;align-items:center;padding-top:18px;text-align:center}
.feature h4{font-size:6.4px;font-weight:600;line-height:1.2;margin-top:8px}
.feature p{font-size:5.2px;color:#777;margin-top:4px;line-height:1.25}
.intro-open{background:#fff;margin-top:9px;padding:8px 10px 0;border-radius:3px}

/* drawer */
.backdrop{position:absolute;inset:0}
.dim{position:absolute;inset:0;background:rgba(0,0,0,.55)}
.drawer{position:absolute;top:0;left:0;bottom:0;width:154px;background:#fff}
.drawer-head{height:32px;display:flex;align-items:center;justify-content:space-between;padding:0 11px;border-bottom:1px solid var(--line);color:var(--red);font-size:8px;font-weight:500}
.drawer-head span{display:flex;align-items:center;gap:5px}
.drawer-head i{font-style:normal;color:#777;font-size:7px}
.group{border-bottom:1px solid var(--line);padding:0 11px}
.group h5{font-size:6.8px;font-weight:600;display:flex;justify-content:space-between;align-items:center;height:24px}
.checks{list-style:none;padding-bottom:8px}
.checks li{font-size:6.6px;display:flex;align-items:center;gap:7px;height:13px}
.checks li::before{content:"";width:7px;height:7px;border:1px solid #444}
.swatches{list-style:none;padding-bottom:9px}
.swatches li{font-size:6.6px;display:flex;align-items:center;gap:7px;height:13px}
.swatches i{width:8px;height:8px;border-radius:50%}
</style>
</head>
<body>

<h1 class="page-title">CATEGORY PRODUCT PAGE</h1>

<!-- Hero banner screen -->
<section class="screen s1">
  <div class="promo"><svg width="9" height="6" viewBox="0 0 9 6"><rect x="0" y="0" width="5.5" height="4" fill="#fff"/><path d="M5.5 1.3h2l1.3 1.5V4H5.5z" fill="#fff"/><circle cx="2" cy="4.8" r="1" fill="#fff"/><circle cx="7" cy="4.8" r="1" fill="#fff"/></svg>FREE DELIVERY £250 UK EX SH&amp;I</div>
  <header class="masthead">
    <div class="brand"><span class="brand-mark"></span>KEELWORTH</div>
    <div class="call"><svg width="12" height="12" viewBox="0 0 12 12" fill="none" stroke="#c8202f" stroke-width="1"><path d="M2 7V6a4 4 0 0 1 8 0v1"/><rect x="1.5" y="6.5" width="2" height="3" rx=".5"/><rect x="8.5" y="6.5" width="2" height="3" rx=".5"/></svg><div>Call us<b>0117 4960 382</b></div></div>
    <div class="cart"><svg width="11" height="11" viewBox="0 0 11 11" fill="none" stroke="#222" stroke-width="1"><rect x="1.5" y="3.5" width="8" height="7" rx="1"/><path d="M3.5 3.5V2.5a2 2 0 0 1 4 0v1"/></svg><i>0</i></div>
  </header>
  <div class="search-row"><div class="burger"><span></span><span></span><span></span></div><div class="search">Search entire store here...<svg width="9" height="9" viewBox="0 0 9 9" fill="none" stroke="#888"><circle cx="4" cy="4" r="3"/><path d="M6.2 6.2 8.5 8.5"/></svg></div></div>
  <div class="usps">
    <div class="rating"><span class="sq"></span>Reviewly <em>4.9</em></div>
    <div class="usp"><svg width="9" height="9" viewBox="0 0 9 9"><rect x="1" y="1" width="7" height="7" fill="none" stroke="#c8202f"/><path d="M3 1v7M5 1v7" stroke="#c8202f"/></svg>FREE FABRICS<br>SAMPLES</div>
    <div class="usp"><svg width="10" height="10" viewBox="0 0 10 10" fill="none" stroke="#c8202f"><path d="M2 8 7 3M6 2l2 2M1.5 8.5l1 -1"/></svg>NATIONWIDE<br>INSTALLATION</div>
  </div>
  <div class="hero">
    <div class="hero-photo" role="img" aria-label="Hotel bedroom interior with full-length flame retardant curtains"></div>
    <div class="hero-copy">
      <div class="hero-rev">Reviewly<small>★★★★★ Excellent</small></div>
      <h1>Flame Retardant Curtains<br>&amp; Fire Resistant Contract<br>Curtains Manufacturers</h1>
      <p>Hotels | Care Homes | Schools | Village<br>HallsBS5867, M1B1, IMO, Certified</p>
      <div class="quote-btn">GET QUICK QUOTE!</div>
    </div>
  </div>
  <div class="trusted">SUPPLYING &amp; TRUSTED BY
    <div class="trusted-row"><span>←</span><span class="partner">Harlow &amp; Finch</span><span class="partner">MARRICK</span><span class="partner box"></span><span>→</span></div>
  </div>
  <div class="toolbar" style="height:40px"><div class="filters-btn"><svg width="9" height="8" viewBox="0 0 9 8" fill="none" stroke="#fff" stroke-width=".9"><path d="M0 1.5h9M0 4h9M0 6.5h9"/><circle cx="3" cy="1.5" r="1" fill="#c8202f"/><circle cx="6" cy="4" r="1" fill="#c8202f"/><circle cx="3" cy="6.5" r="1" fill="#c8202f"/></svg>FILTERS YOUR RESULT</div><div class="sort-btn">Default sorting <svg width="9" height="5" viewBox="0 0 9 5" fill="none" stroke="#fff"><path d="M.5.5 4.5 4.5 8.5.5"/></svg></div></div>
  <nav class="tabbar">
    <div class="tab active"><svg width="14" height="13" viewBox="0 0 14 13" fill="none" stroke="#c8202f"><path d="M1.5 6 7 1l5.5 5v6.5h-11z"/></svg>Home</div>
    <div class="tab"><svg width="13" height="13" viewBox="0 0 13 13" fill="#555"><circle cx="2" cy="2" r="1.2"/><circle cx="6.5" cy="2" r="1.2"/><circle cx="11" cy="2" r="1.2"/><circle cx="2" cy="6.5" r="1.2"/><circle cx="6.5" cy="6.5" r="1.2"/><circle cx="11" cy="6.5" r="1.2"/><circle cx="2" cy="11" r="1.2"/><circle cx="6.5" cy="11" r="1.2"/><circle cx="11" cy="11" r="1.2"/></svg>Category</div>
    <div class="tab"><svg width="13" height="14" viewBox="0 0 13 14" fill="none" stroke="#555"><path d="M1.5 1h7l2.5 2.5V8M1.5 1v12h6"/><circle cx="10" cy="11" r="2.5"/></svg>Quick Quote</div>
    <div class="tab"><svg width="13" height="13" viewBox="0 0 13 13" fill="none" stroke="#555"><circle cx="6.5" cy="4" r="3"/><path d="M1 12.5a5.5 4 0 0 1 11 0z"/></svg>Account</div>
  </nav>
</section>

<!-- Sticky filter bar screen -->
<section class="screen s2">
  <div class="promo"><svg width="9" height="6" viewBox="0 0 9 6"><rect width="5.5" height="4" fill="#fff"/><path d="M5.5 1.3h2l1.3 1.5V4H5.5z" fill="#fff"/><circle cx="2" cy="4.8" r="1" fill="#fff"/><circle cx="7" cy="4.8" r="1" fill="#fff"/></svg>FREE DELIVERY £250 UK EX SH&amp;I</div>
  <header class="masthead">
    <div class="brand"><span class="brand-mark"></span>KEELWORTH</div>
    <div class="call"><svg width="12" height="12" viewBox="0 0 12 12" fill="none" stroke="#c8202f"><path d="M2 7V6a4 4 0 0 1 8 0v1"/><rect x="1.5" y="6.5" width="2" height="3" rx=".5"/><rect x="8.5" y="6.5" width="2" height="3" rx=".5"/></svg><div>Call us<b>0117 4960 382</b></div></div>
    <div class="cart"><svg width="11" height="11" viewBox="0 0 11 11" fill="none" stroke="#222"><rect x="1.5" y="3.5" width="8" height="7" rx="1"/><path d="M3.5 3.5V2.5a2 2 0 0 1 4 0v1"/></svg><i>0</i></div>
  </header>
  <div class="search-row"><div class="burger"><span></span><span></span><span></span></div><div class="search">Search entire store here...<svg width="9" height="9" viewBox="0 0 9 9" fill="none" stroke="#888"><circle cx="4" cy="4" r="3"/><path d="M6.2 6.2 8.5 8.5"/></svg></div></div>
  <div class="usps">
    <div class="rating"><span class="sq"></span>Reviewly <em>4.9</em></div>
    <div class="usp"><svg width="9" height="9" viewBox="0 0 9 9"><rect x="1" y="1" width="7" height="7" fill="none" stroke="#c8202f"/><path d="M3 1v7M5 1v7" stroke="#c8202f"/></svg>FREE FABRICS<br>SAMPLES</div>
    <div class="usp"><svg width="10" height="10" viewBox="0 0 10 10" fill="none" stroke="#c8202f"><path d="M2 8 7 3M6 2l2 2M1.5 8.5l1-1"/></svg>NATIONWIDE<br>INSTALLATION</div>
  </div>
  <div class="toolbar"><div class="filters-btn"><svg width="9" height="8" viewBox="0 0 9 8" fill="none" stroke="#fff" stroke-width=".9"><path d="M0 1.5h9M0 4h9M0 6.5h9"/><circle cx="3" cy="1.5" r="1" fill="#c8202f"/><circle cx="6" cy="4" r="1" fill="#c8202f"/><circle cx="3" cy="6.5" r="1" fill="#c8202f"/></svg>FILTERS YOUR RESULT</div><div class="sort-btn">Default sorting <svg width="9" height="5" viewBox="0 0 9 5" fill="none" stroke="#fff"><path d="M.5.5 4.5 4.5 8.5.5"/></svg></div></div>
  <div class="listing">
    <div class="crumb">Home / Flame Retardant / <b>Flame Retardant Curtains</b></div>
    <div class="intro"><span>Introduction to our flame retardant curtains -<br>Click for more information</span><svg width="11" height="11" viewBox="0 0 11 11" fill="none" stroke="#c8202f"><circle cx="5.5" cy="5.5" r="4.8"/><path d="M5.5 3v5M3 5.5h5"/></svg></div>
    <div class="count">Products 1 to 12 of 234 total</div>
    <div class="cards">
      <article class="card"><span class="badge new">NEW</span>
        <div class="card-photo" role="img" aria-label="Botanical leaf print curtains in a living room" style="background:linear-gradient(135deg,#2f4a3c,#7a8f78 55%,#c8c3b8)"></div>
        <h3>Botanical Garden Print Flame Retardant Curtains</h3>
        <div class="stars">★★★★★ <span>(1)</span></div>
        <div class="price">Excl. Tax: <b>£66.66</b><br>Incl. Tax: <b>£79.99</b></div>
      </article>
      <article class="card"><span class="badge best">BEST SELLER</span>
        <div class="card-photo" role="img" aria-label="Grey plain curtains with fabric colour swatches" style="background:linear-gradient(135deg,#4a4a4a,#8d8d8d 55%,#3d5a7a)"></div>
        <h3>Botanical Garden Print Flame Retardant Curtains</h3>
        <div class="stars">★★★★★ <span>(1)</span></div>
        <div class="price">Excl. Tax: <b>£66.66</b><br>Incl. Tax: <b>£79.99</b></div>
      </article>
    </div>
  </div>
  <nav class="tabbar">
    <div class="tab active"><svg width="14" height="13" viewBox="0 0 14 13" fill="none" stroke="#c8202f"><path d="M1.5 6 7 1l5.5 5v6.5h-11z"/></svg>Home</div>
    <div class="tab"><svg width="13" height="13" viewBox="0 0 13 13" fill="#555"><circle cx="2" cy="2" r="1.2"/><circle cx="6.5" cy="2" r="1.2"/><circle cx="11" cy="2" r="1.2"/><circle cx="2" cy="6.5" r="1.2"/><circle cx="6.5" cy="6.5" r="1.2"/><circle cx="11" cy="6.5" r="1.2"/><circle cx="2" cy="11" r="1.2"/><circle cx="6.5" cy="11" r="1.2"/><circle cx="11" cy="11" r="1.2"/></svg>Category</div>
    <div class="tab"><svg width="13" height="14" viewBox="0 0 13 14" fill="none" stroke="#555"><path d="M1.5 1h7l2.5 2.5V8M1.5 1v12h6"/><circle cx="10" cy="11" r="2.5"/></svg>Quick Quote</div>
    <div class="tab"><svg width="13" height="13" viewBox="0 0 13 13" fill="none" stroke="#555"><circle cx="6.5" cy="4" r="3"/><path d="M1 12.5a5.5 4 0 0 1 11 0z"/></svg>Account</div>
  </nav>
</section>

<!-- Toggle detail screen -->
<section class="screen s3">
  <div class="promo"><svg width="9" height="6" viewBox="0 0 9 6"><rect width="5.5" height="4" fill="#fff"/><path d="M5.5 1.3h2l1.3 1.5V4H5.5z" fill="#fff"/><circle cx="2" cy="4.8" r="1" fill="#fff"/><circle cx="7" cy="4.8" r="1" fill="#fff"/></svg>FREE DELIVERY £250 UK EX SH&amp;I</div>
  <header class="masthead">
    <div class="brand"><span class="brand-mark"></span>KEELWORTH</div>
    <div class="call"><svg width="12" height="12" viewBox="0 0 12 12" fill="none" stroke="#c8202f"><path d="M2 7V6a4 4 0 0 1 8 0v1"/><rect x="1.5" y="6.5" width="2" height="3" rx=".5"/><rect x="8.5" y="6.5" width="2" height="3" rx=".5"/></svg><div>Call us<b>0117 4960 382</b></div></div>
    <div class="cart"><svg width="11" height="11" viewBox="0 0 11 11" fill="none" stroke="#222"><rect x="1.5" y="3.5" width="8" height="7" rx="1"/><path d="M3.5 3.5V2.5a2 2 0 0 1 4 0v1"/></svg><i>0</i></div>
  </header>
  <div class="search-row"><div class="burger"><span></span><span></span><span></span></div><div class="search">Search entire store here...<svg width="9" height="9" viewBox="0 0 9 9" fill="none" stroke="#888"><circle cx="4" cy="4" r="3"/><path d="M6.2 6.2 8.5 8.5"/></svg></div></div>
  <div class="usps">
    <div class="rating"><span class="sq"></span>Reviewly <em>4.9</em></div>
    <div class="usp"><svg width="9" height="9" viewBox="0 0 9 9"><rect x="1" y="1" width="7" height="7" fill="none" stroke="#c8202f"/><path d="M3 1v7M5 1v7" stroke="#c8202f"/></svg>FREE FABRICS<br>SAMPLES</div>
    <div class="usp"><svg width="10" height="10" viewBox="0 0 10 10" fill="none" stroke="#c8202f"><path d="M2 8 7 3M6 2l2 2M1.5 8.5l1-1"/></svg>NATIONWIDE<br>INSTALLATION</div>
  </div>
  <div class="toolbar"><div class="filters-btn"><svg width="9" height="8" viewBox="0 0 9 8" fill="none" stroke="#fff" stroke-width=".9"><path d="M0 1.5h9M0 4h9M0 6.5h9"/><circle cx="3" cy="1.5" r="1" fill="#c8202f"/><circle cx="6" cy="4" r="1" fill="#c8202f"/><circle cx="3" cy="6.5" r="1" fill="#c8202f"/></svg>FILTERS YOUR RESULT</div><div class="sort-btn">Default sorting <svg width="9" height="5" viewBox="0 0 9 5" fill="none" stroke="#fff"><path d="M.5.5 4.5 4.5 8.5.5"/></svg></div></div>
  <div class="listing">
    <div class="crumb">Home / Flame Retardant / <b>Flame Retardant Curtains</b></div>
    <div class="intro-open">
      <div style="display:flex;justify-content:space-between;align-items:center;font-size:6.6px;color:#555;line-height:1.25"><span>Introduction to our flame retardant curtains -<br>Click for more information</span><svg width="11" height="11" viewBox="0 0 11 11" fill="none" stroke="#c8202f"><circle cx="5.5" cy="5.5" r="4.8"/><path d="M3 5.5h5"/></svg></div>
      <div class="features">
        <div class="feature"><svg width="20" height="20" viewBox="0 0 20 20" fill="none" stroke="#c8202f" stroke-width="1.2"><circle cx="10" cy="10" r="9"/><path d="M10 4c2 3 4 4 4 7a4 4 0 0 1-8 0c0-2 1-3 2-4 0 2 1 2 2 2 0-2-1-3 0-5z"/></svg><h4>FIRE RETARDANT<br>BS5867 &amp; OTHER<br>CODES</h4><p>Suitable for<br>Commercial Use.</p></div>
        <div class="feature"><svg width="20" height="20" viewBox="0 0 20 20" fill="none" stroke="#c8202f" stroke-width="1.2"><path d="M3 3v14h14z"/><path d="M6 10v5h5z"/><path d="M5 6h2M5 9h2M9 13v2M12 15v-2"/></svg><h4>MADE TO MEASURE</h4><p>All Curtains are Made<br>to Measure to your<br>exact requirements.</p></div>
        <div class="feature"><svg width="20" height="20" viewBox="0 0 20 20" fill="none" stroke="#222" stroke-width="1.2"><rect x="2" y="12" width="12" height="5"/><path d="M4 12 13 3l4 4-7 5"/><path d="M4 14.5h2M8 14.5h2" stroke="#c8202f"/></svg><h4>100S DESIGNS &amp;<br>COLOURS</h4></div>
        <div class="feature"><svg width="20" height="20" viewBox="0 0 20 20" fill="none" stroke="#222" stroke-width="1.2"><rect x="3" y="2" width="14" height="16" rx="1"/><path d="M3 5.5h14"/><circle cx="10" cy="12" r="4" stroke="#c8202f"/></svg><h4>WASHABLE</h4><p>Depending on Lining</p></div>
      </div>
    </div>
  </div>
  <nav class="tabbar">
    <div class="tab active"><svg width="14" height="13" viewBox="0 0 14 13" fill="none" stroke="#c8202f"><path d="M1.5 6 7 1l5.5 5v6.5h-11z"/></svg>Home</div>
    <div class="tab"><svg width="13" height="13" viewBox="0 0 13 13" fill="#555"><circle cx="2" cy="2" r="1.2"/><circle cx="6.5" cy="2" r="1.2"/><circle cx="11" cy="2" r="1.2"/><circle cx="2" cy="6.5" r="1.2"/><circle cx="6.5" cy="6.5" r="1.2"/><circle cx="11" cy="6.5" r="1.2"/><circle cx="2" cy="11" r="1.2"/><circle cx="6.5" cy="11" r="1.2"/><circle cx="11" cy="11" r="1.2"/></svg>Category</div>
    <div class="tab"><svg width="13" height="14" viewBox="0 0 13 14" fill="none" stroke="#555"><path d="M1.5 1h7l2.5 2.5V8M1.5 1v12h6"/><circle cx="10" cy="11" r="2.5"/></svg>Quick Quote</div>
    <div class="tab"><svg width="13" height="13" viewBox="0 0 13 13" fill="none" stroke="#555"><circle cx="6.5" cy="4" r="3"/><path d="M1 12.5a5.5 4 0 0 1 11 0z"/></svg>Account</div>
  </nav>
</section>

<!-- Off-canvas filters screen -->
<section class="screen s4">
  <div class="backdrop">
    <div class="promo">FREE DELIVERY £250 UK EX SH&amp;I</div>
    <header class="masthead">
      <div class="brand"><span class="brand-mark"></span>KEELWORTH</div>
      <div class="call"><div>Call us<b>0117 4960 382</b></div></div>
      <div class="cart"><svg width="11" height="11" viewBox="0 0 11 11" fill="none" stroke="#222"><rect x="1.5" y="3.5" width="8" height="7" rx="1"/><path d="M3.5 3.5V2.5a2 2 0 0 1 4 0v1"/></svg><i>0</i></div>
    </header>
    <div class="search-row"><div class="burger"><span></span><span></span><span></span></div><div class="search"><span></span><svg width="9" height="9" viewBox="0 0 9 9" fill="none" stroke="#888"><circle cx="4" cy="4" r="3"/><path d="M6.2 6.2 8.5 8.5"/></svg></div></div>
    <div class="usps" style="justify-content:flex-end"><div class="usp">NATIONWIDE<br>INSTALLATION</div></div>
    <div class="hero" style="height:235px">
      <div class="hero-photo" role="img" aria-label="Hotel bedroom interior with full-length flame retardant curtains"></div>
      <div class="hero-copy" style="align-items:flex-end;padding:70px 10px 0 0;text-align:right"><h1 style="font-size:13px">Curtains<br>Contract<br>Manufacturers</h1><p>| Village<br>Certified</p></div>
    </div>
    <div class="toolbar"><div class="filters-btn"></div><div class="sort-btn">Default sorting</div></div>
    <div class="dim"></div>
  </div>
  <aside class="drawer">
    <div class="drawer-head"><span><svg width="9" height="8" viewBox="0 0 9 8" fill="none" stroke="#c8202f" stroke-width=".9"><path d="M0 1.5h9M0 4h9M0 6.5h9"/><circle cx="3" cy="1.5" r="1" fill="#fff"/><circle cx="6" cy="4" r="1" fill="#fff"/><circle cx="3" cy="6.5" r="1" fill="#fff"/></svg>FILTERS</span><i>X</i></div>
    <div class="group"><h5>CATEGORIES</h5>
      <ul class="checks"><li>Plans &amp; Semi Plains</li><li>Printed &amp; FR Curtains</li><li>Woven FR Curtains</li><li>Voile &amp; Seer Curtains</li><li>Budget</li><li>Shower</li><li>European M1-B1 Standard</li><li>IMO Curtains</li><li>All Ranges</li></ul>
    </div>
    <div class="group"><h5>FEATURE <svg width="5" height="8" viewBox="0 0 5 8" fill="none" stroke="#222"><path d="M.5.5 4 4 .5 7.5"/></svg></h5></div>
    <div class="group"><h5>COLOR <svg width="8" height="5" viewBox="0 0 8 5" fill="none" stroke="#222"><path d="M.5.5 4 4 7.5.5"/></svg></h5>
      <ul class="swatches">
        <li><i style="background:#1f5a85"></i>Blue</li><li><i style="background:#f3e7c6"></i>Cream</li><li><i style="background:#ec3d7d"></i>Pink Purple</li><li><i style="background:#fbf3da"></i>Natural</li><li><i style="background:#d9a92c"></i>Yellow</li><li><i style="background:#118a3d"></i>Green</li><li><i style="background:#7d0b0b"></i>Red</li><li><i style="background:#b3b3b3"></i>Grey</li>
      </ul>
    </div>
    <div class="group" style="border:0"><h5>FABRIC STYLE <svg width="5" height="8" viewBox="0 0 5 8" fill="none" stroke="#222"><path d="M.5.5 4 4 .5 7.5"/></svg></h5></div>
  </aside>
</section>

<p class="caption" style="left:57px">HERO BANNER</p>
<p class="caption" style="left:333px;top:646px">STICKY TOP &nbsp;FILTER BAR</p>
<p class="caption" style="left:591px;top:655px">TOGGLE DETAIL INFORMATION</p>
<p class="caption" style="left:860px;top:657px;width:260px">AJAX FILTERS SELECT DROPDOWN</p>

</body>
</html>
```